Modern Attractive Letterhead for Veterinary House Call Business.

A letterhead which can be printed on A4, A5 and A6 paper sizes.
To have: ( our files to be uploaded)
1. Logo with Text
2. telephone
3. email
4. website
5. Address

Target Market(s)

60-85year mainly women pet owners. Also market include families, young professionals, busy people who have dogs and cats

Industry/Entity Type

Business

Requirements
Must have
• 1. Logo with Text ( provided)
• 2. telephone
• 3. email
• 4. website
• 5. Address
Nice to have
• Needs to be modern, preferably warm and caring in nature( if possible )
Should not have
• difficulty in printing A5 and A6

```html
<!DOCTYPE html>
<html lang="en">
<head>
<meta charset="utf-8">
<title>Hearthside Vet Care — Letterhead</title>
<link rel="stylesheet" href="https://fonts.googleapis.com/css2?family=Crimson+Pro:wght@400;600&display=swap">
<style>
  :root {
    --ink-navy: #2d3a8c;
    --brand-blue: #2a6fb5;
    --paper: #ffffff;
    --watermark: #e8e8e8;
  }
  * { margin: 0; padding: 0; box-sizing: border-box; }
  html, body { width: 848px; height: 1200px; overflow: hidden; background: var(--paper); }
  .letterhead {
    position: relative;
    width: 848px;
    height: 1200px;
    overflow: hidden;
    background: var(--paper);
    font-family: "Crimson Pro", "Palatino Linotype", serif;
    color: var(--ink-navy);
  }
  .brand {
    position: absolute;
    left: 62px;
    top: 40px;
    display: flex;
    align-items: center;
    gap: 22px;
  }
  .brand-mark {
    width: 72px;
    height: 72px;
    border-radius: 50%;
    background: var(--brand-blue);
  }
  .brand-name {
    font-weight: 600;
    font-size: 46px;
    letter-spacing: 1px;
    color: var(--ink-navy);
    line-height: 1;
  }
  .corner-decoration {
    position: absolute;
    left: 430px;
    top: 640px;
    width: 520px;
    height: 520px;
    border-radius: 50%;
    background: var(--watermark);
  }
  .contact-list {
    position: absolute;
    left: 36px;
    top: 1046px;
    list-style: none;
  }
  .contact-item {
    display: flex;
    align-items: center;
    height: 23.5px;
    font-size: 14.5px;
  }
  .contact-icon {
    width: 20px;
    height: 18px;
    margin-right: 20px;
    fill: var(--ink-navy);
  }
</style>
</head>
<body>
  <main class="letterhead">
    <header class="brand">
      <div class="brand-mark"></div>
      <span class="brand-name">Hearthside Vet Care</span>
    </header>

    <div class="corner-decoration"></div>

    <ul class="contact-list">
      <li class="contact-item">
        <svg class="contact-icon" viewBox="0 0 20 18" aria-hidden="true">
          <path d="M10 1a5.5 5.5 0 0 0-5.5 5.5C4.5 10.5 10 17 10 17s5.5-6.5 5.5-10.5A5.5 5.5 0 0 0 10 1zm0 7.6a2.1 2.1 0 1 1 0-4.2 2.1 2.1 0 0 1 0 4.2z"/>
        </svg>
        PO Box 4821 Kenmore Hills QLD 4069
      </li>
      <li class="contact-item">
        <svg class="contact-icon" viewBox="0 0 20 18" aria-hidden="true">
          <path d="M2 4h16v10H2z" fill="none" stroke="currentColor"/>
          <path d="M2 4h16v1.2L10 10.5 2 5.2z"/>
          <path d="M2 14l6-5 1 .7-6 5.3zM18 14l-6-5-1 .7 6 5.3z"/>
        </svg>
        hello@hearthsidevet.com.au
      </li>
      <li class="contact-item">
        <svg class="contact-icon" viewBox="0 0 20 18" aria-hidden="true">
          <path d="M5.2 1.5l2.6 3.2-1.6 2a10 10 0 0 0 5 5l2-1.6 3.3 2.6-1.4 2.6C9.5 15.7 3.8 10 3 3z"/>
        </svg>
        0400123987
      </li>
      <li class="contact-item">
        <svg class="contact-icon" viewBox="0 0 20 18" aria-hidden="true">
          <circle cx="10" cy="9" r="8"/>
          <path d="M6 5.5c1.5 0 2.5 1 2 2.5s-2 1.5-1.5 3 1 2.5.5 4M12.5 3.5c-.5 1.5.5 2.5 2 2.5s1.5 2 .5 3-1.5 2.5-.5 4" fill="none" stroke="#fff" stroke-width="1.4"/>
        </svg>
        www.hearthsidevet.com.au
      </li>
    </ul>
  </main>
</body>
</html>
```